Aquaponic greenhouse needs a business brochure that shows what a unique system we have

We would like to expand our marketing beyond social media. We are a aquaponic greenhouse where we use fish to fertilize the water so that we don't have to use any chemicals in the system. This method is sustainable and environmentally friendly. We grow in a climate controlled system year round and deliver the freshest produce directly to our local families, schools and restaurants. All of our produce is grown from seed, closely monitored during the growing cycle, hand picked and hand packaged for our customers.

Aquaponics - The combination of Aquaculture (raising fish) and Hydroponics (growing plants in a soilless system)

Sustainable - Closed loop system using the same water for the fish and plants.

Local - Delaware natives providing healthy eating opportunities for our neighbors throughout the state.

Chemical and Soil Free

Largest in the First State - With over 15,000 square feet of a climate controlled environment, we can grow the freshest produce year round with consistent output.

Target Market(s)

Customers and those who don’t use social media

Industry/Entity Type

Agribusiness

Font styles to use
Sans Serif

Colors
0255a3
32b8a4
9bcb3c
cadf82

Requirements
Must have
• Our logo (attached) some personalized pictures (can be found on our website www.quillmeadowgrow.com) and areas where we can customize our written content. Must have editable text and be able to replace pictures as we grow.
Nice to have
• Options for a tri-fold and bi-fold brochures

```html
<!DOCTYPE html>
<html lang="en">
<head>
<meta charset="utf-8">
<title>Quill Meadow Grow – Brochure</title>
<link href="https://fonts.googleapis.com/css2?family=Cabin:wght@600;700&family=Mulish:wght@400;600&family=Barlow:wght@500;600&display=swap" rel="stylesheet">
<style>
:root{
  --backdrop:#e8875a;
  --navy:#0255a3;
  --teal:#32b8a4;
  --lime:#9bcb3c;
  --pale:#cadf82;
  --panel-light:#8fd39a;
  --panel-mid:#5cc58a;
  --panel-deep:#2fae6e;
  --ink:#111a14;
  --white:#ffffff;
}
*{box-sizing:border-box;margin:0;padding:0}
html,body{width:1200px;height:436px;overflow:hidden;background:var(--backdrop)}
body{position:relative;font-family:"Mulish",sans-serif;color:var(--ink)}
.spread{position:absolute;top:33px;width:505px;height:357px;overflow:hidden}
.spread--outside{left:70px}
.spread--inside{left:625px}
.panel{position:absolute;top:0;width:253px;height:357px;overflow:hidden}
.block{position:absolute;left:0;width:100%}
.green{background:linear-gradient(135deg,var(--panel-light),var(--panel-mid))}
.green-deep{background:linear-gradient(160deg,var(--panel-mid),var(--panel-deep))}
.photo{position:absolute;left:0;width:100%}
h2,h3{font-family:"Cabin",sans-serif;font-weight:700;color:var(--ink)}
/* news */
.news{top:0;height:105px;padding:8px 0 0 14px}
.news h2{font-size:14px;margin-bottom:6px}
.news-grid{display:grid;grid-template-columns:116px 110px;column-gap:6px;row-gap:3px}
.news h3{font-size:7.4px;margin-bottom:2px}
.news p{font-size:4.5px;line-height:1.5}
.largest{top:105px;height:99px;padding:9px 30px 0 29px;background:linear-gradient(135deg,#a6dba2,#8ed39d)}
.largest h2{font-size:13px;margin-bottom:6px}
.largest p{font-size:6.6px;line-height:1.4}
.team-photo{top:204px;height:153px;background:linear-gradient(180deg,#c9ced2 0%,#9aa3aa 35%,#2a5fc4 70%,#1e4fae 100%)}
.contact{position:absolute;left:22px;top:7px;width:211px;height:39px;background:var(--white);display:flex;align-items:center;gap:6px;padding:0 5px}
.contact .brand{width:57px;font-family:"Mulish",sans-serif;font-weight:600;font-size:7.6px;line-height:1.1;color:var(--navy);text-align:center;display:flex;align-items:center;gap:3px}
.contact .brand i{display:block;width:6px;height:6px;border-radius:50%;background:var(--navy);flex:none}
.contact h3{font-size:10.5px;margin-bottom:2px}
.contact p{font-size:6.2px;line-height:1.5}
/* cover */
.cover-photo{top:0;height:223px;background:linear-gradient(120deg,#e8eef2 0%,#9cc7d6 30%,#3f86c8 55%,#6cc78d 100%)}
.offering{position:absolute;left:122px;top:113px;width:116px;text-align:center;font-family:"Cabin",sans-serif;font-weight:700;font-size:19px;line-height:21px;color:var(--white);letter-spacing:.6px;text-shadow:0 0 2px #2a6f55,0 0 2px #2a6f55}
.brand-band{top:223px;height:68px;background:#4aa577;display:flex;align-items:center;justify-content:center;gap:6px}
.brand-band span{font-family:"Mulish",sans-serif;font-weight:600;font-size:17px;color:var(--navy)}
.brand-band i{width:14px;height:14px;border-radius:50%;background:var(--navy)}
.delivery{top:291px;height:66px;display:flex;align-items:center;justify-content:center;text-align:center;font-family:"Cabin",sans-serif;font-weight:600;font-size:13px;line-height:1.3;color:var(--white);letter-spacing:.4px}
/* inside */
.tank-photo{top:0;height:143px;background:linear-gradient(135deg,#2b6fc9 0%,#4a8fd8 40%,#3a4a44 70%,#6b7a72 100%)}
.bees{top:143px;height:101px;padding:4px 20px 0 12px}
.bees h3{font-size:10px;margin-bottom:3px}
.bees p{font-size:7.8px;line-height:1.3}
.bee-photo{top:244px;height:113px;background:linear-gradient(135deg,#c9a15a,#8a5a1e 50%,#d8b870)}
.products{top:0;height:96px;padding:10px 0 0 12px}
.products h2{font-family:"Barlow",sans-serif;font-weight:600;font-size:10.5px;letter-spacing:.5px;margin-bottom:6px}
.products ul{display:grid;grid-template-columns:118px 110px;list-style:none;font-family:"Barlow",sans-serif;font-weight:500;font-size:8px;line-height:11.6px;letter-spacing:.3px}
.products li::before{content:"";display:inline-block;width:3px;height:3px;border-radius:50%;background:var(--ink);margin:0 7px 1.5px 0;vertical-align:middle}
.greens-photo{top:96px;height:164px;background:linear-gradient(160deg,#aeb8bc 0%,#7d8b8e 30%,#3f9a3c 60%,#2c7a27 100%)}
.locally{top:260px;height:97px;padding:8px 12px 0 30px;text-align:right}
.locally h3{font-size:10.3px;line-height:1.25;margin:0 0 3px 6px}
.locally p{font-size:7.4px;line-height:1.3}
</style>
</head>
<body>

<section class="spread spread--outside">
  <div class="panel" style="left:0">
    <div class="block news green">
      <h2>See us in the News</h2>
      <div class="news-grid">
        <div>
          <h3>Channel 9 Riverside</h3>
          <p>Watch our interview with Channel 9 News out of Riverside to see a slightly different perspective of our process.</p>
        </div>
        <div>
          <h3>First State Courier</h3>
          <p>Our local community is the best! The outpouring of support we receive is amazing.</p>
        </div>
        <div>
          <h3>Kent County Ledger</h3>
          <p>What do fish poop and lettuce have in common? Find out what The Kent County Ledger says.</p>
        </div>
        <div>
          <h3>National News</h3>
          <p>This article is featured in The Capital Herald, Bay City Chronicle, National Weekly Report, and at least 20 other National news feeds.</p>
        </div>
      </div>
    </div>
    <div class="block largest">
      <h2>Largest in the 1st State!</h2>
      <p>We are the largest commercial Aquaponics greenhouse in Delaware! With over 15,000 square feet of space, we offer lettuces, greens and fish year-round directly to consumers and to local schools and restaurants. Check out our products page to see what is currently available for pickup throughout the First State.</p>
    </div>
    <div class="photo team-photo" role="img" aria-label="Photo of the greenhouse team standing among blue fish tanks">
      <div class="contact">
        <div class="brand"><i></i>Quill Meadow Grow</div>
        <div>
          <h3>contact us</h3>
          <p>Quill Meadow Grow, 418 Fernbrook Ln,<br>Millbrook, VT 05762, US. Ph: (802) 555-0147</p>
        </div>
      </div>
    </div>
  </div>

  <div class="panel" style="left:252px">
    <div class="photo cover-photo" role="img" aria-label="Photo of the owner holding a news microphone in front of the delivery van"></div>
    <div class="offering">WE ARE<br>NOW<br>OFFERING</div>
    <div class="block brand-band"><i></i><span>Quill Meadow Grow</span></div>
    <div class="block delivery green-deep">PERSONALIZED DELIVERY<br>ON ORDERS TOTALING<br>$100 OR MORE</div>
  </div>
</section>

<section class="spread spread--inside">
  <div class="panel" style="left:0">
    <div class="photo tank-photo" role="img" aria-label="Photo of the grower feeding fish in a blue aquaculture tank"></div>
    <div class="block bees green">
      <h3>The Bees’ Knees</h3>
      <p>We have harvested our first batch of honey! Our bees enjoyed working their magic over our clover, wild flowers and corn this Spring and Summer and we would like to share their love with you. Their honey came straight from the hives, we strained it (without heat), and bottled it by hand for you to enjoy all of the health benefits of their hard work. We are selling our limited selection of liquid gold on our Products page.</p>
    </div>
    <div class="photo bee-photo" role="img" aria-label="Close-up photo of honey bees on a hive frame"></div>
  </div>

  <div class="panel" style="left:252px">
    <div class="block products green">
      <h2>PRODUCTS</h2>
      <ul>
        <li>Summer Crisp Lettuce.</li>
        <li>Swiss Chard</li>
        <li>Romaine Lettuce.</li>
        <li>Raw Honey 16 oz.</li>
        <li>Wildfire Lettuce Mix.</li>
        <li>QMG Tee Lt Blue</li>
        <li>Waldmann’s Lettuce.</li>
        <li>QMG Tee Navy</li>
        <li>Kale.</li>
        <li>QMG Koozie</li>
      </ul>
    </div>
    <div class="photo greens-photo" role="img" aria-label="Photo of the grower tending rows of leafy lettuce in the greenhouse"></div>
    <div class="block locally green-deep">
      <h3>Locally Grown, Sustainable produce including multiple varieties of lettuce.</h3>
      <p>Our building is up, we are finishing some final touches inside and we are producing locally grown, fresh, soil-free produce daily. Follow us here and on social media to discover where you can find our products.</p>
    </div>
  </div>
</section>

</body>
</html>
```